Book cover design for 'Harbour Lantern' novel

Title of book 'Harbour Lantern'
Subtitle 'a Owen Tessary novel'
Author 'K L Dunmore'
Book genre 'novel - adventure'
Format ' eBook, paperback, audio, thumbnail'
Type 'Self-publishing through RVN'
Trim size 6 x 9
Back cover 'Seeking redemption on the Via de la Plata.
Owen Tessary’s life changed forever in a moment of madness. Haunted by his crime, Owen feels a calling to seek redemption on the Camino de Santiago.
The daily toil of walking the Via de la Plata from Seville causes Owen to search his soul.
On The Way Owen encounters other pilgrims with their own personal reasons to answer the call of the camino.
Join Owen for the many highs and lows of camino life as he moves step by step closer to his goal.
Can the Camino give Owen peace of mind and stop his nightmares?'
Overall vision 'The front cover at the top should be the title:
Camino
Calling
This will fill about 20 per cent of the front cover. It must be centre justified. The title should use the same type face as the official Camino de Santiago road sign (see first download). The type should be in bright blue. The background should be in bright yellow.
Under the title should be an image of a path stretching to the horizon with the shadow of a pilgrim (see second download).
Superimposed on the image should be the words 'a Owen Tessary novel' maybe using a type face similar to the street signage used in Spain (see third download).
At the bottom of the front cover should be the author's name 'Karl Dunmore' in the same style as the blue and yellow title - BUT MUCH SMALLER.
On the SPINE of the book should be 'Harbour Lantern' and 'Karl Dunmore' in the blue text on yellow background.
On the back cover there should be a photograph (see fourth download) with the text UPDATE ON THE TEXT 'Seeking redemption on the Via de la Plata.
In a moment of madness Owen Tessary’s life changed forever. Haunted by his atrocious act, he feels a calling to seek redemption on the Camino de Santiago.
The daily slog of walking the Via de la Plata from Seville causes Owen to search deep within his soul.
On The Way Owen encounters other pilgrims with their own personal reasons to answer the call of the Camino.
Can the Camino give Owen peace of mind and stop his nightmares?' with a three centimetre space at the bottom for bar code/ISBN and the author headshot photograph attached.
Updates

Target Market(s)

Readers who have walked the Camino de Santiago in Spain or who are interested

Requirements
Nice to have
• I would like my headshot (attached) included on the back cover

```html
<!DOCTYPE html>
<html lang="en">
<head>
<meta charset="utf-8">
<title>Harbour Lantern – Front Cover</title>
<link href="https://fonts.googleapis.com/css2?family=Inter:wght@400;500;700;800;900&display=swap" rel="stylesheet">
<style>
  :root {
    --cover-yellow-light: #f9c95c;
    --cover-yellow: #f0ae2a;
    --cover-yellow-deep: #e39e1f;
    --title-blue: #0a8bd6;
    --title-blue-light: #35a5e0;
    --subtitle-white: #ffffff;
    --sky-top: #9fb8a8;
    --sky-warm: #e2c29a;
    --hills: #6f8a55;
    --field: #5f8a2e;
    --field-deep: #3f6a1f;
  }
  * { margin: 0; padding: 0; box-sizing: border-box; }
  html, body {
    width: 910px;
    height: 1200px;
    overflow: hidden;
    background: #ffffff;
  }
  .cover {
    position: relative;
    width: 910px;
    height: 1200px;
    background: linear-gradient(135deg, var(--cover-yellow-light) 0%, var(--cover-yellow) 45%, var(--cover-yellow-deep) 100%);
    font-family: "Inter", "Helvetica Neue", Arial, sans-serif;
    overflow: hidden;
  }
  .cover-title {
    position: absolute;
    top: 34px;
    left: 0;
    width: 100%;
    text-align: center;
    color: var(--title-blue);
    font-weight: 900;
    font-size: 158px;
    line-height: 0.98;
    letter-spacing: -0.045em;
    background: linear-gradient(135deg, var(--title-blue-light) 0%, var(--title-blue) 40%);
    -webkit-background-clip: text;
    background-clip: text;
    -webkit-text-fill-color: transparent;
  }
  .cover-title span { display: block; }
  .cover-subtitle {
    position: absolute;
    top: 382px;
    left: 0;
    width: 100%;
    text-align: center;
    color: var(--subtitle-white);
    font-weight: 500;
    font-size: 50px;
    letter-spacing: -0.01em;
  }
  .rule {
    position: absolute;
    left: 0;
    width: 100%;
    height: 11px;
    background: var(--title-blue);
  }
  .rule-top { top: 478px; }
  .rule-bottom { top: 1058px; }
  .cover-photo {
    position: absolute;
    top: 489px;
    left: 0;
    width: 100%;
    height: 569px;
    background:
      linear-gradient(180deg,
        var(--sky-top) 0%,
        var(--sky-warm) 40%,
        #d9c6a4 50%,
        var(--hills) 56%,
        var(--field) 68%,
        var(--field-deep) 100%);
  }
  .cover-author {
    position: absolute;
    top: 1082px;
    left: 0;
    width: 100%;
    text-align: center;
    color: var(--title-blue);
    font-weight: 700;
    font-size: 68px;
    letter-spacing: -0.02em;
  }
</style>
</head>
<body>
  <main class="cover">
    <h1 class="cover-title"><span>Harbour</span><span>Lantern</span></h1>
    <p class="cover-subtitle">a Owen Tessary novel</p>
    <div class="rule rule-top"></div>
    <div class="cover-photo" role="img" aria-label="Photograph of a gravel pilgrim path stretching through green fields to distant hills under a cloudy sky, with the shadow of a walking pilgrim on the path"></div>
    <div class="rule rule-bottom"></div>
    <p class="cover-author">Karl Dunmore</p>
  </main>
</body>
</html>
```